Vornithex Page Design

Hi, I am looking for someone who would help us make killer web page designs. There are 3 main pages that need to be designed:
1. Homepage-- Take a look at current design being worked on:
http://dev.vornithex.example/newsite/consumer.php#firstPage/1
2. Listing Page-- This is the current one being worked on: http://dev.vornithex.example/newsite/listing.php
The old one: http://www.vornithex.example/dentist
3. Profile Page:
The old design: http://www.vornithex.example/dentist/dentistprofile/Dr-Milo-Tansey-DDS-Escondido-CA/92025/id/10009
We are looking for someone who can take these designs to the next level and also provide an intuitive user interphase to help consumers and professionals navigate through the site appropriately and efficiently.
Our goal is to help guide users to help understand their values while educating them on the proper values that they need to look for. Creating trust and credibility is of most importance.
All designs must be mobile/desktop/tablet compatible
Target Market(s)
Professionals and Consumers, ages 25-55

```html
<!DOCTYPE html>
<html lang="en">
<head>
<meta charset="utf-8">
<title>Vornithex – Rank, compare, select</title>
<link href="https://fonts.googleapis.com/css2?family=Open+Sans:wght@300;400;600;700&display=swap" rel="stylesheet">
<style>
  :root{
    --blue:#0f62ab;
    --blue-dark:#0b4f8d;
    --blue-mid:#1a73c4;
    --blue-light:#2f8fdc;
    --ink:#1d1d1d;
    --text:#2b2b2b;
    --muted:#8a8a8a;
    --tab-grey:#dedede;
    --white:#ffffff;
    --footer-link:#b8cde4;
  }
  *{box-sizing:border-box;margin:0;padding:0}
  html,body{width:726px;height:1200px;overflow:hidden;background:var(--white)}
  body{position:relative;font-family:"Open Sans",Arial,sans-serif;color:var(--text)}
  .abs{position:absolute}

  /* top bar */
  .topbar{left:0;top:0;width:726px;height:23px;background:var(--blue);color:var(--white);font-size:8px}
  .topbar .tagline{position:absolute;left:47px;top:6px;font-weight:600}
  .topbar .account{position:absolute;right:86px;top:6px;font-weight:700}
  .topbar .help{position:absolute;right:26px;top:6px;font-weight:700}
  .topbar svg{vertical-align:-2px;margin-left:2px}

  /* header */
  .brand{left:47px;top:48px;font-size:19px;font-weight:300;color:#333;letter-spacing:-.3px}
  .brand-dot{display:inline-block;width:7px;height:7px;border-radius:50%;background:var(--blue);margin-right:5px;vertical-align:3px}
  .main-nav{left:220px;top:55px;display:flex;font-size:8.5px;font-weight:700;color:#222}
  .main-nav span{padding:0 12px;border-left:1px solid #cfcfcf;line-height:16px}
  .main-nav span:first-child{border:0;padding-left:0;color:var(--blue)}
  .search{left:522px;top:50px;width:128px;height:20px;border:1px solid #8fb4d6;border-radius:3px;background:#e9f0f7;font-size:8px;font-style:italic;color:#777;padding:4px 7px}
  .search svg{position:absolute;right:6px;top:4px}
  .advanced{left:660px;top:55px;font-size:8px;color:#4a8ccc}

  /* hero */
  .hero{left:47px;top:99px;width:648px;height:286px;border:2px solid var(--blue-light);overflow:hidden}
  .hero-pro{left:0;top:0;width:328px;height:282px;background:linear-gradient(90deg,#fafafa,#eceef0 45%,#f6f6f6)}
  .hero-con{left:328px;top:0;width:316px;height:282px;background:linear-gradient(120deg,#f6ece4,#d9a57f 45%,#b97a50 80%,#e9d4c2)}
  .hero-tab{top:196px;color:var(--white);font-size:12.5px;font-weight:700}
  .hero-tab .label{position:absolute;top:20px}
  .arrow-btn{width:28px;height:28px;border-radius:50%;background:var(--blue-mid);border:2px solid #0a3f73;box-shadow:0 1px 2px rgba(0,0,0,.3)}
  .arrow-btn svg{position:absolute;left:6px;top:8px}

  /* section headings */
  .section-title{left:0;width:726px;text-align:center;font-size:16.5px;color:var(--ink)}
  .section-title .accent{color:var(--blue-mid)}
  .title-rule{left:283px;width:160px;height:8px}

  /* features */
  .lead{left:47px;top:468px;font-size:10px;font-weight:700;color:#111}
  .body-copy{font-size:7.4px;line-height:9.4px;color:#222;text-align:justify}
  .read-more{left:47px;top:589px;width:84px;height:17px;border-radius:3px;background:var(--blue);color:var(--white);font-size:7.5px;font-weight:600;padding:3px 0 0 27px}
  .read-more svg{position:absolute;left:12px;top:6px}
  .feature-photo{left:503px;top:453px;width:192px;height:176px;background:radial-gradient(circle at 35% 35%,#f3e3c9,#e7e2dc 50%,#f4f5f7 80%);border-radius:4px}

  /* tab band */
  .band{left:0;top:660px;width:726px;height:51px;background:var(--blue)}
  .band-tab{top:15px;height:24px;border-radius:3px;background:var(--tab-grey);font-size:8px;font-weight:600;color:#222;text-align:center;line-height:24px;box-shadow:inset 0 -2px 0 #bdbdbd}
  .band-tab.is-active{background:var(--blue-mid);color:var(--white);border:1px solid #d6e6f6;box-shadow:none;line-height:22px}

  /* about */
  .avatar{left:333px;top:760px;width:84px;height:84px;border-radius:50%;border:2px solid var(--blue-light);background:radial-gradient(circle at 50% 40%,#e6d2c2,#b9c3cc 60%,#e9edf1)}
  .question-pill{left:271px;top:919px;width:179px;height:18px;border-radius:3px;background:var(--blue-mid);color:var(--white);font-size:9.5px;font-weight:700;text-align:center;line-height:18px}
  .checklist{font-size:8px;color:#222}
  .checklist li{list-style:none;height:17px;display:flex;align-items:center}
  .checklist svg{margin-right:6px}

  /* footer */
  .footer{left:0;top:1103px;width:726px;height:97px;background:var(--blue-dark)}
  .footer h4{position:absolute;font-size:9.5px;font-weight:700;color:var(--white)}
  .footer-links{position:absolute;font-size:8px;color:var(--footer-link);line-height:16.5px}
  .footer-links .current{color:var(--white)}
  .social{position:absolute;left:503px;top:48px;display:flex;gap:5px}
  .social span{width:22px;height:22px;background:#8c8f93;border-radius:1px;display:block}
  .social span.is-lit{background:#2d9ee0}
</style>
</head>
<body>

<header>
  <div class="abs topbar">
    <span class="tagline">Rank, compare, select- the professional way</span>
    <span class="account">Login/Register
      <svg width="9" height="9" viewBox="0 0 10 10"><circle cx="5" cy="3" r="2.3" fill="#fff"/><path d="M1 10c0-3 2-4.5 4-4.5S9 7 9 10z" fill="#fff"/></svg></span>
    <span class="help"><svg width="9" height="9" viewBox="0 0 10 10"><circle cx="5" cy="5" r="4.6" fill="#fff"/><text x="5" y="8" font-size="7" font-weight="700" text-anchor="middle" fill="#0f62ab" font-family="Open Sans,sans-serif">?</text></svg> Help</span>
  </div>

  <div class="abs brand"><span class="brand-dot"></span>vornithex</div>

  <nav class="abs main-nav">
    <span>RANKINGS</span><span>FEATURES</span><span>ABOUT US</span>
  </nav>

  <div class="abs search">Search
    <svg width="10" height="10" viewBox="0 0 10 10"><circle cx="4" cy="4" r="3" fill="none" stroke="#111" stroke-width="1.6"/><path d="M6.2 6.2L9 9" stroke="#111" stroke-width="1.8"/></svg>
  </div>
  <div class="abs advanced">Advanced</div>
</header>

<section class="abs hero">
  <div class="abs hero-pro" role="img" aria-label="Photo of a smiling doctor in a white coat with a stethoscope"></div>
  <div class="abs hero-con" role="img" aria-label="Close-up photo of a young woman with long auburn hair"></div>

  <div class="abs hero-tab" style="left:0;width:260px;height:60px">
    <svg class="abs" width="260" height="60" viewBox="0 0 260 60"><path d="M0 0H205C236 0 256 26 258 60H0Z" fill="#1a6ec0"/></svg>
    <span class="label" style="left:29px">FOR PROFESSIONAL</span>
    <svg class="abs" style="left:169px;top:19px" width="26" height="18" viewBox="0 0 26 18"><path d="M2 8l6-5 5 3 5-3 6 5-8 8-3-3-3 3z" fill="#0b2f55"/><path d="M9 9l3 3M12 8l3 3" stroke="#1a6ec0" stroke-width="1.2"/></svg>
  </div>

  <div class="abs hero-tab" style="left:386px;width:258px;height:60px">
    <svg class="abs" width="258" height="60" viewBox="0 0 258 60"><path d="M258 0H55C24 0 4 26 0 60H258Z" fill="#1a6ec0"/></svg>
    <svg class="abs" style="left:70px;top:20px" width="26" height="17" viewBox="0 0 26 17"><circle cx="7" cy="4.5" r="3" fill="#0b2f55"/><circle cx="19" cy="4.5" r="3" fill="#0b2f55"/><circle cx="13" cy="5.5" r="3.4" fill="#0b2f55"/><path d="M1 16c0-5 3-7 6-7s6 2 6 7zM13 16c0-5 3-7 6-7s6 2 6 7z" fill="#0b2f55"/><path d="M6 17c0-5 3-7.5 7-7.5s7 2.5 7 7.5z" fill="#0b2f55"/></svg>
    <span class="label" style="left:101px">FOR CONSUMERS</span>
  </div>
</section>
<div class="abs arrow-btn" style="left:360px;top:362px"><svg width="13" height="9" viewBox="0 0 13 9"><path d="M1 1.5l5.5 5.5L12 1.5" fill="none" stroke="#fff" stroke-width="1.8"/></svg></div>

<section>
  <h2 class="abs section-title" style="top:409px;font-weight:400">VORNITHEX <span class="accent">FEATURES</span></h2>
  <svg class="abs title-rule" style="top:432px" viewBox="0 0 160 8"><path d="M0 .5H160" stroke="#2f8fdc" stroke-width="1"/><path d="M73 0H87L80 7Z" fill="#1a73c4"/></svg>

  <p class="abs lead">Vornithex is a new way to discover the right professionals for every need and situation.</p>
  <p class="abs body-copy" style="left:47px;top:489px;width:421px">Unlike traditional search engines and rating sites, Vornithex tracks and ranks a very large amount of information - and makes that information available to you. Professional are encouraged to tell you their stories in ways that appeal clearly and specifically to your needs. This way, professionals can closely target consumers who share their values and business philosophies and consumers can find professionals who match their needs precisely.</p>
  <p class="abs body-copy" style="left:47px;top:547px;width:421px">When you select an industry and specialty from Vornithex's menu you'll first see professionals who are ranked the highest overall in your local area. You'll be able to see how they compare with other professionals in a number of different, important areas. Choosing a professional from this list is a sure bet to getting quality products and services.</p>
  <div class="abs read-more"><svg width="8" height="5" viewBox="0 0 8 5"><path d="M0 0H8L4 5Z" fill="#fff"/></svg>Read More</div>

  <div class="abs feature-photo" role="img" aria-label="Photo of a smiling woman in a light blue shirt beside a laptop showing the rankings listing"></div>
</section>
<div class="abs arrow-btn" style="left:360px;top:627px"><svg width="13" height="9" viewBox="0 0 13 9"><path d="M1 1.5l5.5 5.5L12 1.5" fill="none" stroke="#fff" stroke-width="1.8"/></svg></div>

<nav class="abs band">
  <div class="abs band-tab is-active" style="left:188px;width:70px">ABOUT</div>
  <div class="abs band-tab" style="left:268px;width:71px">TEAM</div>
  <div class="abs band-tab" style="left:349px;width:94px">ADVISORY&nbsp; BOARD</div>
  <div class="abs band-tab" style="left:452px;width:71px">CORE VALUES</div>
</nav>

<section>
  <h2 class="abs section-title" style="top:724px;font-size:13.5px;font-weight:400"><span class="accent">ABOUT</span> VORNITHEX</h2>
  <svg class="abs title-rule" style="top:743px" viewBox="0 0 160 8"><path d="M0 .5H160" stroke="#2f8fdc" stroke-width="1"/><path d="M73 0H87L80 7Z" fill="#1a73c4"/></svg>
  <div class="abs avatar" role="img" aria-label="Portrait photo of a smiling man in a grey suit"></div>

  <p class="abs body-copy" style="left:47px;top:859px;width:648px;font-size:7.7px">Until now it's been impossible to find, compare and select high-quality professionals based on your personal needs and values without someone else's marketing agenda getting in the way. Typical review sites tell you someone else's experienced (perceived value) but say nothing about quality of the products and services they received.</p>
  <p class="abs body-copy" style="left:47px;top:896px;font-size:7.7px">You can now find professionals based on quality ratings, customized to your own values.</p>

  <div class="abs question-pill">What's most important to you?</div>

  <ul class="abs checklist" style="left:113px;top:947px">
    <li><svg width="9" height="9" viewBox="0 0 9 9"><rect x=".5" y="1.5" width="7" height="7" fill="none" stroke="#1a73c4"/><path d="M2 4.5l2 2L8.5 1" fill="none" stroke="#1a73c4" stroke-width="1.5"/></svg>Price?</li>
    <li><svg width="9" height="9" viewBox="0 0 9 9"><rect x=".5" y="1.5" width="7" height="7" fill="none" stroke="#1a73c4"/><path d="M2 4.5l2 2L8.5 1" fill="none" stroke="#1a73c4" stroke-width="1.5"/></svg>Actual work examples?</li>
    <li><svg width="9" height="9" viewBox="0 0 9 9"><rect x=".5" y="1.5" width="7" height="7" fill="none" stroke="#1a73c4"/><path d="M2 4.5l2 2L8.5 1" fill="none" stroke="#1a73c4" stroke-width="1.5"/></svg>Location?</li>
  </ul>
  <ul class="abs checklist" style="left:286px;top:947px">
    <li><svg width="9" height="9" viewBox="0 0 9 9"><rect x=".5" y="1.5" width="7" height="7" fill="none" stroke="#1a73c4"/><path d="M2 4.5l2 2L8.5 1" fill="none" stroke="#1a73c4" stroke-width="1.5"/></svg>Quality Ranking?</li>
    <li><svg width="9" height="9" viewBox="0 0 9 9"><rect x=".5" y="1.5" width="7" height="7" fill="none" stroke="#1a73c4"/><path d="M2 4.5l2 2L8.5 1" fill="none" stroke="#1a73c4" stroke-width="1.5"/></svg>Years in business?</li>
    <li><svg width="9" height="9" viewBox="0 0 9 9"><rect x=".5" y="1.5" width="7" height="7" fill="none" stroke="#1a73c4"/><path d="M2 4.5l2 2L8.5 1" fill="none" stroke="#1a73c4" stroke-width="1.5"/></svg>"Hospitality" consumer ratings?</li>
  </ul>
  <ul class="abs checklist" style="left:454px;top:945px">
    <li><svg width="9" height="9" viewBox="0 0 9 9"><rect x=".5" y="1.5" width="7" height="7" fill="none" stroke="#1a73c4"/><path d="M2 4.5l2 2L8.5 1" fill="none" stroke="#1a73c4" stroke-width="1.5"/></svg>Industry professional recommendation?</li>
  </ul>

  <p class="abs body-copy" style="left:47px;top:1014px;font-size:7.7px">Vornithex gives you this power! You control what's important and find professionals ranked based by what's important to YOU.</p>
  <p class="abs body-copy" style="left:47px;top:1033px;width:648px;font-size:7.7px">Cut through the clutter, eliminate the guessing game and display what is most important to you in selecting professional. Compare apples to apples by ranking objectively and accurately.</p>
  <p class="abs body-copy" style="left:47px;top:1066px;width:648px;font-size:7.7px">Vornithex give you the power to be a smart shopper to compare and select more specifically and precisely than ever before. Professionals now can reach consumer who share the values of what they do best.</p>
</section>

<footer class="abs footer">
  <h4 style="left:83px;top:15px">COMPANY</h4>
  <div class="footer-links" style="left:83px;top:38px">Home<br><span class="current">About</span><br>FAQ</div>
  <div class="footer-links" style="left:150px;top:38px">Login<br>Register<br>Contact Us</div>
  <div class="footer-links" style="left:240px;top:38px">Terms of Use<br>Privacy Policy</div>
  <h4 style="left:498px;top:15px">CONNECT</h4>
  <div class="social" aria-label="Social links">
    <span></span><span class="is-lit"></span><span></span><span></span><span></span><span></span>
  </div>
</footer>
<div class="abs arrow-btn" style="left:360px;top:1091px"><svg width="13" height="9" viewBox="0 0 13 9"><path d="M1 1.5l5.5 5.5L12 1.5" fill="none" stroke="#fff" stroke-width="1.8"/></svg></div>

</body>
</html>
```